International Consultancy Needs Slick Professional Presentation Graphic

Quarvel are an international engineering and advisory consultancy servicing the mining industry with a mix of Technology (Software), Services (consulting) and Systems (work structures).

We need a slick presentation graphic for use in presentation slides, whitepapers. I have attached a basic pic of the information we want to convey. Flat or 3D no preference, colouring no preference. Don't have to be circles, that was just easiest to draft up initially.

Industry/Entity Type

Mining

```html
<!DOCTYPE html>
<html lang="en">
<head>
<meta charset="utf-8">
<title>Capability Model</title>
<link href="https://fonts.googleapis.com/css2?family=Jost:wght@600;700&display=swap" rel="stylesheet">
<style>
  :root {
    --bg-light: #f7f8f8;
    --bg-dark: #e3e6e6;
    --orange: #ff7d0c;
    --yellow: #f4dc40;
    --beige: #f5ebe1;
    --green-light: #80ff12;
    --green-dark: #009406;
    --blush: #fde8ec;
    --mint: #eefaf4;
    --cyan-light: #88fcfc;
    --cyan: #00f3f7;
    --ink: #111111;
    --white: #ffffff;
    --people-ink: #a4501c;
    --org-ink: #1877e2;
    --shade: rgba(60, 70, 70, 0.35);
  }
  html, body {
    margin: 0;
    padding: 0;
    width: 1200px;
    height: 1200px;
    overflow: hidden;
  }
  .canvas {
    width: 1200px;
    height: 1200px;
    background: radial-gradient(circle at 50% 45%, var(--bg-light) 0%, var(--bg-light) 45%, var(--bg-dark) 100%);
  }
  .capability-model {
    display: block;
    width: 1200px;
    height: 1200px;
  }
  .facet { stroke: none; }
  .facet--orange { fill: var(--orange); }
  .facet--yellow { fill: var(--yellow); }
  .facet--beige { fill: var(--beige); }
  .facet--green-light { fill: var(--green-light); }
  .facet--green-dark { fill: var(--green-dark); }
  .facet--blush { fill: var(--blush); }
  .facet--mint { fill: var(--mint); }
  .facet--cyan-light { fill: var(--cyan-light); }
  .facet--cyan { fill: var(--cyan); }
  .guide-line {
    stroke: rgba(120, 130, 130, 0.18);
    stroke-width: 3;
  }
  .label {
    font-family: "Jost", "Futura", sans-serif;
    font-weight: 700;
    text-anchor: middle;
  }
  .label--sub {
    font-size: 33px;
    fill: var(--white);
    letter-spacing: 0.5px;
  }
  .label--pillar {
    font-size: 38px;
    fill: var(--white);
  }
  .label--people {
    font-size: 38px;
    fill: var(--people-ink);
  }
  .label--org {
    font-size: 33px;
    fill: var(--org-ink);
  }
  .label--core {
    font-size: 40px;
    fill: var(--ink);
    stroke: var(--white);
    stroke-width: 1.5px;
    paint-order: stroke;
  }
</style>
</head>
<body>
<div class="canvas">
  <svg class="capability-model" viewBox="0 0 1350 1350" xmlns="http://www.w3.org/2000/svg" role="img" aria-label="Capability model: Technology, People and Systems around Capability">
    <defs>
      <filter id="facet-shadow" x="-20%" y="-20%" width="140%" height="140%">
        <feDropShadow dx="0" dy="6" stdDeviation="8" flood-color="#3c4646" flood-opacity="0.3"/>
      </filter>
      <filter id="text-shadow" x="-10%" y="-30%" width="120%" height="160%">
        <feDropShadow dx="1" dy="2" stdDeviation="1.5" flood-color="#000" flood-opacity="0.3"/>
      </filter>
    </defs>

    <g class="guides">
      <line class="guide-line" x1="430" y1="230" x2="555" y2="433"/>
      <line class="guide-line" x1="930" y1="120" x2="970" y2="190"/>
      <line class="guide-line" x1="1110" y1="433" x2="1220" y2="620"/>
      <line class="guide-line" x1="60" y1="550" x2="130" y2="675"/>
      <line class="guide-line" x1="130" y1="675" x2="60" y2="800"/>
      <line class="guide-line" x1="275" y1="918" x2="350" y2="1050"/>
      <line class="guide-line" x1="555" y1="918" x2="410" y2="1170"/>
      <line class="guide-line" x1="1110" y1="918" x2="1220" y2="720"/>
      <line class="guide-line" x1="970" y1="1160" x2="930" y2="1230"/>
    </g>

    <g class="cluster cluster--people" filter="url(#facet-shadow)">
      <polygon class="facet facet--beige" points="555,433 830,433 970,675 690,675"/>
      <polygon class="facet facet--orange" points="690,190 970,190 830,433 555,433"/>
      <polygon class="facet facet--yellow" points="970,190 1110,433 970,675 830,433"/>
    </g>

    <g class="cluster cluster--technology" filter="url(#facet-shadow)">
      <polygon class="facet facet--blush" points="555,433 690,675 555,918 415,675"/>
      <polygon class="facet facet--green-light" points="275,433 555,433 415,675 130,675"/>
      <polygon class="facet facet--green-dark" points="130,675 415,675 555,918 275,918"/>
    </g>

    <g class="cluster cluster--systems" filter="url(#facet-shadow)">
      <polygon class="facet facet--mint" points="690,675 970,675 830,918 555,918"/>
      <polygon class="facet facet--cyan-light" points="970,675 1110,918 970,1160 830,918"/>
      <polygon class="facet facet--cyan" points="555,918 830,918 970,1160 690,1160"/>
    </g>

    <g class="labels">
      <text class="label label--sub" x="743" y="272" filter="url(#text-shadow)">User</text>
      <text class="label label--sub" x="743" y="312" filter="url(#text-shadow)">Interface</text>
      <text class="label label--sub" x="743" y="353" filter="url(#text-shadow)">Engineering</text>

      <text class="label label--people" x="968" y="455">PEOPLE</text>

      <text class="label label--pillar" x="340" y="567" filter="url(#text-shadow)">TECNOLOGY</text>

      <text class="label label--sub" x="344" y="760" filter="url(#text-shadow)">System</text>
      <text class="label label--sub" x="344" y="800" filter="url(#text-shadow)">Interface</text>
      <text class="label label--sub" x="344" y="841" filter="url(#text-shadow)">Engineering</text>

      <text class="label label--core" x="697" y="682">CAPABILITY</text>

      <text class="label label--org" x="970" y="926">Organisation</text>
      <text class="label label--org" x="970" y="966">Design</text>

      <text class="label label--pillar" x="762" y="1066" filter="url(#text-shadow)">SYSTEMS</text>
    </g>
  </svg>
</div>
</body>
</html>
```